Inspirational Quote Poster for Employees

For this project, we need a simple yet high-impact poster template that will be customized for each of our employees with a personalized inspirational quote and color scheme. This template should allow us to quickly and easily customize the text and colors in the poster without a lot of effort.

The poster design should consist of:
- A stylized text area to contain the main text of the quote
- A separate text area to contain the source of quote
- A background that complements the color and style of the text

Text may use different typographic effects (such as color, stroke weight, italicization, font size changes, drop shadows) to draw attention to words in the quote; the source of the quote may be formatted the same as the main text of the quote, or may be formatted differently to distinguish it from the main quote.

The background may be simply a single color, subtle texture, gradients, halftone effects, or other color/texture effects may be used to complement the text.

Examples of the types of posters envisioned by this project:
- http://www.pinvelora.example/marcusdtelford/quillbase-job-1/

Sample quotes to use to build your poster - choose whichever one you want, but be certain that the poster design will handle both long and short quotes:
- "Happiness in intelligent people is the rarest thing I know" - Walden Prosket
- "Wanting to be someone else is a waste of the person you are." - Rolf Dintey
- "Experience is not what happens to you. It is what you do with what happens to you." - Ferris Mundell
- "Simplicity is the ultimate in sophistication." - Rinaldo de Pavesco
- "You will get all you want in life if you help enough other people get what they want." - Tad Pomfrey
- "Hell, there are no rules here — we're trying to accomplish something." - Gareth Vullane

Industry/Entity Type

Quote

Requirements
Must have
• Final deliverable must be:
• - Formatted for an 18” x 24” poster (in portrait orientation)
• - Delivered in Adobe InDesign, Adobe Illustrator, or Extended PostScript format
• - Use CMYK color mode
• - Be print-ready at 300dpi resolution
• - Include any fonts used in the template

```html
<!DOCTYPE html>
<html lang="en">
<head>
<meta charset="utf-8">
<title>Simplicity – Inspirational Quote Poster</title>
<link rel="stylesheet" href="https://fonts.googleapis.com/css2?family=Anton&family=Source+Sans+3:wght@300;400&display=swap">
<style>
  :root {
    --backdrop: #2b2b2b;
    --poster-paper: #d3c4ad;
    --accent-circle: #6bb0b3;
    --frame-line: #5b4d45;
    --headline-white: #ffffff;
    --secondary-teal: #0e5a5c;
    --source-teal: #1d5a5d;
  }
  html, body {
    margin: 0;
    padding: 0;
    width: 1200px;
    height: 1000px;
    overflow: hidden;
    background: var(--backdrop);
  }
  .poster-canvas {
    display: block;
    width: 1200px;
    height: 1000px;
  }
  .poster-sheet { fill: var(--poster-paper); }
  .accent-circle { fill: var(--accent-circle); }
  .quote-frame {
    fill: none;
    stroke: var(--frame-line);
    stroke-width: 2;
  }
  .quote-emphasis {
    font-family: "Anton", "Impact", sans-serif;
    fill: var(--headline-white);
  }
  .quote-emphasis--lead { font-size: 74px; }
  .quote-emphasis--close { font-size: 58px; }
  .quote-connector {
    font-family: "Source Sans 3", "Myriad Pro", sans-serif;
    font-weight: 300;
    font-size: 44px;
    fill: var(--secondary-teal);
  }
  .quote-source {
    font-family: "Source Sans 3", "Myriad Pro", sans-serif;
    font-weight: 400;
    font-size: 15px;
    fill: var(--source-teal);
  }
</style>
</head>
<body>
  <svg class="poster-canvas" viewBox="0 0 1200 1000" xmlns="http://www.w3.org/2000/svg" aria-labelledby="poster-title">
    <title id="poster-title">Simplicity is the ultimate in sophistication — Rinaldo de Pavesco</title>
    <rect class="poster-sheet" x="304" y="79" width="595" height="841"/>
    <circle class="accent-circle" cx="602" cy="498" r="260"/>
    <rect class="quote-frame" x="381" y="316" width="442" height="442"/>

    <g class="quote-block">
      <text class="quote-emphasis quote-emphasis--lead" x="418" y="480" textLength="358" lengthAdjust="spacingAndGlyphs">SIMPLICITY</text>
      <text class="quote-connector" x="419" y="537" textLength="360" lengthAdjust="spacingAndGlyphs">IS THE ULTIMATE IN</text>
      <text class="quote-emphasis quote-emphasis--close" x="418" y="606" textLength="365" lengthAdjust="spacingAndGlyphs">SOPHISTICATION</text>
      <text class="quote-source" x="783" y="638" text-anchor="end">Rinaldo de Pavesco</text>
    </g>
  </svg>
</body>
</html>
```